Corporate business card

Business card design for IT consultancy company.
Clients are larger companies.
Card should have round edges on some or all.
Make the user stop and look at the card.
Steel grey background. But if you have a better idea, show me.
Target Market(s)
Corporate - a but web 2.0
Industry/Entity Type
Business
Contact Information for Business Card
As per design.
Font styles to use
Other font styles liked:
- Helvetica
Colors
5c5c5c
ec2027
ffffff
Requirements
Must have
- Clean design - follow brivo styles
- text in white
- Lets have a conversation in red
- Powered by passion in red
Nice to have
- Uncluttered
Should not have
- Cluttered

```html
<!DOCTYPE html>
<html lang="en">
<head>
<meta charset="utf-8">
<title>Kavel Partners – Business Card</title>
<link rel="stylesheet" href="https://fonts.googleapis.com/css2?family=Arimo:ital,wght@0,400;1,400&family=Roboto+Condensed:wght@300;400;700&display=swap">
<style>
  :root {
    --backdrop: #fdf0fd;
    --card: #bfbfbf;
    --ink: #5c5c5c;
    --accent: #a50f14;
    --white: #ffffff;
    --icon: #8e8e8e;
  }
  * { margin: 0; padding: 0; box-sizing: border-box; }
  html, body { width: 1200px; height: 801px; overflow: hidden; }
  body { background: var(--backdrop); position: relative; font-family: "Arimo", Arial, sans-serif; }

  .card { position: absolute; width: 312px; height: 514px; background: var(--card); }
  .card--back { left: 278px; top: 136px; border-radius: 0 40px 0 40px; }
  .card--front { left: 610px; top: 138px; border-radius: 40px 0 40px 0; }

  .wordmark {
    position: absolute; left: 0; width: 100%; text-align: center;
    font-family: "Roboto Condensed", Arial, sans-serif; font-weight: 700;
    line-height: 1; letter-spacing: 1px;
  }
  .card--back .wordmark { top: 180px; font-size: 34px; color: var(--ink); }
  .card--front .wordmark { top: 96px; font-size: 38px; color: var(--accent); }
  .wordmark .dot { display: inline-block; width: 10px; height: 10px; background: currentColor; margin-right: 8px; vertical-align: middle; }

  .tagline {
    position: absolute; top: 300px; left: 0; width: 100%; text-align: center;
    font-style: italic; font-size: 14px; color: var(--accent); letter-spacing: 0.3px;
  }

  .identity { position: absolute; left: 33px; top: 261px; font-family: "Roboto Condensed", Arial, sans-serif; color: var(--ink); }
  .identity .name { font-weight: 700; font-size: 21px; line-height: 24px; }
  .identity .role { font-weight: 300; font-size: 22px; line-height: 26px; letter-spacing: 0.3px; }

  .contacts { position: absolute; left: 32px; top: 324px; list-style: none; }
  .contacts li { display: flex; align-items: center; height: 17.5px; color: var(--white); font-size: 12.5px; letter-spacing: 0.6px; }
  .contacts li.spaced { letter-spacing: 4px; }
  .contacts svg { width: 12px; height: 12px; margin-right: 6px; flex: none; }

  .call-to-action {
    position: absolute; top: 435px; left: 55px;
    font-family: "Roboto Condensed", Arial, sans-serif; font-size: 16px;
    color: var(--accent); letter-spacing: 0.3px;
  }
</style>
</head>
<body>
  <section class="card card--back">
    <div class="wordmark"><span class="dot"></span>KAVEL PARTNERS</div>
    <p class="tagline">POWERED BY PASSION !</p>
  </section>

  <section class="card card--front">
    <div class="wordmark"><span class="dot"></span>KAVEL PARTNERS</div>

    <div class="identity">
      <p class="name">DANA WHITFIELD</p>
      <p class="role">MANAGING PARTNER</p>
    </div>

    <ul class="contacts">
      <li>
        <svg viewBox="0 0 12 12"><path d="M1 6 6 1.5 11 6H9.5v4.5h-7V6Z" fill="var(--icon)"/></svg>
        +61390001234
      </li>
      <li class="spaced">
        <svg viewBox="0 0 12 12"><rect x="3" y="1" width="6" height="10" rx="1" fill="none" stroke="var(--icon)" stroke-width="1.4"/></svg>
        0400551 28
      </li>
      <li>
        <svg viewBox="0 0 12 12"><rect x="1.5" y="1.5" width="9" height="9" rx="1.5" fill="var(--icon)"/><rect x="4" y="4" width="4" height="4" fill="var(--card)"/></svg>
        DANA_WHITFIELD
      </li>
      <li>
        <svg viewBox="0 0 12 12"><rect x="1.5" y="1.5" width="9" height="9" rx="1.5" fill="var(--icon)"/><rect x="3.5" y="5" width="5" height="2" fill="var(--card)"/></svg>
        WWW.KAVELPARTNERS.COM.AU
      </li>
      <li>
        <svg viewBox="0 0 12 12"><rect x="1" y="2.5" width="10" height="7" fill="var(--icon)"/><path d="M1 2.5 6 6.5 11 2.5" fill="none" stroke="var(--card)" stroke-width="1"/></svg>
        DANA@KAVELPARTNERS.COM.AU
      </li>
    </ul>

    <p class="call-to-action">LET'S HAVE A CONVERSATION !</p>
  </section>
</body>
</html>
```